https://www.kreidetafel.de - a website for school website in germany for presentation/paper download

we own the webpage https://www.kreidetafel.de and we need a new webdesign (a new website logo is also possible). we want only new images and css, we don´t want to made any change to the HTML code.
we need only new images/color for a new modern look.

we want to have more trust to our user. they have to download presentation/paper
we need template for this sites:
https://www.kreidetafel.de/
https://www.kreidetafel.de/referate/englisch
https://www.kreidetafel.de/forum.php
https://www.kreidetafel.de/forum/insektenhotel/147503
https://www.kreidetafel.de/referat/latein/sokrates/14781
https://www.kreidetafel.de/schule_seminararbeit_fachliste.php?fach=127
and other sites on the website. (take a look around the website)

we don´t like white color for sublines or text. (h1/h2/strong) . in image are white Text OK.

important: we want to chance ONLY the CSS and PICS, we don´t want to remove or chance any HTML code.

after you have made a mockup of the new design and we give you a go, you have to made a package with the IMAGES and the CSS rules (text how we have to chance the current css)

Target Market(s)

Germany, Austria, Switzerland -DACH

Industry/Entity Type

School

Coding

Coded - Design and coding required

Number of Pages Required

5+ page

Font styles to use
Serif
Sans Serif

Colors

Designer to choose colors to be used in the design.

Requirements
Must have
• We want only to remove images and no HTML Code
Should not have
• NO white colors for Text on the site. In images are OK

```html
<!DOCTYPE html>
<html lang="en">
<head>
<meta charset="utf-8">
<title>Kreidetafel.de – Start Page</title>
<link href="https://fonts.googleapis.com/css2?family=Noto+Serif&family=Roboto:wght@400;500&family=Roboto+Condensed:wght@400;500&family=Open+Sans:wght@400&display=swap" rel="stylesheet">
<style>
:root{
  --sky:#6ccbe4;
  --sky-light:#8fd8ec;
  --grass:#8cc34a;
  --grass-dark:#6aa63a;
  --blue:#0d5cb6;
  --blue-dark:#0a4a94;
  --green:#8cc34a;
  --olive:#6e8a1f;
  --orange:#e8761c;
  --text:#333;
  --muted:#555;
  --panel:#f4f4f4;
  --line:#dcdcdc;
  --footer:#2b2b2b;
  --white:#fff;
}
*{box-sizing:border-box;margin:0;padding:0}
html,body{width:1033px;height:1200px;overflow:hidden}
body{position:relative;font-family:"Roboto",sans-serif;color:var(--text);
  background:linear-gradient(var(--sky) 0,var(--sky-light) 760px,var(--grass) 900px,var(--grass-dark) 1200px)}
.scenery{position:absolute;left:0;top:880px;width:1033px;height:320px;
  background:linear-gradient(#9fd25a,var(--grass-dark))}
.page{position:absolute;left:101px;top:43px;width:831px;height:1101px;background:var(--white)}
.abs{position:absolute}

/* header */
.brand{left:15px;top:40px;display:flex;align-items:center;gap:49px}
.brand-mark{width:40px;height:34px;background:#1b1b1b}
.brand-name{font-family:"Noto Serif",serif;font-size:34px;color:#1a4f9c;line-height:1}
.tagline{left:104px;top:80px;font-size:8.5px;color:#222;font-family:"Roboto",sans-serif}
.phone{left:603px;top:55px;display:flex;align-items:center;gap:8px;font-style:italic;font-size:13px;color:#555}
.login{left:748px;top:50px;width:69px;height:26px;background:var(--blue);color:var(--white);
  font:500 12px "Roboto Condensed",sans-serif;display:flex;align-items:center;justify-content:center;gap:5px}

/* nav */
.nav{left:13px;top:118px;width:804px;height:40px;background:var(--blue);display:flex;align-items:center}
.nav a{color:var(--white);text-decoration:none;font:400 12.5px "Roboto Condensed",sans-serif;
  height:40px;display:flex;align-items:center;padding:0 18px;border-right:1px solid rgba(255,255,255,.15)}
.nav .social{position:absolute;left:676px;top:14px;display:flex;gap:6px}
.nav .social span{width:11px;height:11px;background:var(--white);border-radius:2px}
.nav .searchcap{position:absolute;right:0;top:0;width:66px;height:40px;background:var(--green);
  clip-path:polygon(22px 0,100% 0,100% 100%,0 100%)}

/* side boxes */
.box{position:absolute;width:168px;background:var(--panel);border:1px solid var(--line)}
.box-head{position:relative;height:32px;background:var(--blue);color:var(--white);
  font:500 12px "Roboto Condensed",sans-serif;display:flex;align-items:center;padding-left:11px}
.box-head .cap{position:absolute;right:0;top:0;width:34px;height:32px;background:var(--green);
  clip-path:polygon(10px 0,100% 0,100% 100%,0 100%)}
.box-head .cap svg{position:absolute;right:7px;top:8px}
.list{list-style:none}
.list li{height:27.4px;display:flex;align-items:center;padding-left:22px;font-size:10.5px;color:#333;
  border-bottom:1px solid var(--line);position:relative}
.list li:last-child{border-bottom:0}
.list li::before{content:"";position:absolute;left:11px;top:50%;margin-top:-3.5px;border-left:4px solid #333;
  border-top:3.5px solid transparent;border-bottom:3.5px solid transparent}
.list li .num{position:absolute;left:115px}

/* center */
.hero{left:203px;top:184px;width:425px;height:174px;
  background:radial-gradient(ellipse at 50% 30%,#8a7a5c 0,#4a4a3a 45%,#1e1e1a 100%)}
.hero-search{position:absolute;left:28px;top:74px;width:370px;height:41px;border:1px solid #777;
  background:rgba(0,0,0,.55);display:flex;align-items:center;gap:8px;padding-left:9px}
.hero-search label{color:var(--white);font:400 11px "Roboto Condensed",sans-serif}
.hero-search .field{width:216px;height:26px;background:var(--white);border-radius:2px;font-size:6.5px;
  color:#555;display:flex;align-items:center;padding-left:8px}
.hero-search .btn{width:76px;height:26px;background:var(--green);color:var(--white);
  font:500 11px "Roboto Condensed",sans-serif;display:flex;align-items:center;justify-content:center}
.tree{left:207px;top:397px;width:164px;height:168px;
  background:radial-gradient(circle at 50% 40%,#f2b8a8 0,#e8e8ef 55%,#fff 75%)}
.hello h1{position:absolute;left:397px;top:406px;font:400 26px "Roboto",sans-serif;color:#333}
.hello p{position:absolute;left:398px;top:450px;width:215px;font:400 9px/17px "Open Sans",sans-serif;color:#333}
.hello .hl{color:var(--orange);font-size:10.5px}
.hello .lk{color:var(--blue);font-size:10.5px}

.subjects{left:203px;top:602px;width:425px;height:273px;background:var(--panel);border:1px solid var(--line)}
.subjects .box-head{font-size:11.5px}
.col{position:absolute;top:14px;list-style:none}
.col li{height:24px;display:flex;align-items:center;padding-left:13px;font:400 9px "Open Sans",sans-serif;position:relative}
.col li::before{content:"";position:absolute;left:3px;top:9px;border-left:3.5px solid #333;
  border-top:3px solid transparent;border-bottom:3px solid transparent}

/* right */
.msg-body{height:106px;text-align:center;font-size:10.5px;line-height:15px;padding-top:26px;color:#333}
.msg-body a{color:var(--blue);text-decoration:none}
.msg-foot{border-top:1px solid var(--line);height:34px;display:flex;align-items:center;justify-content:center;font-size:10.5px}
.promo{left:650px;top:377px;width:168px;height:213px;background:var(--olive)}
.promo h3{height:34px;display:flex;align-items:center;justify-content:center;color:var(--white);
  font:400 16px "Roboto",sans-serif}
.promo .photo{height:130px;background:linear-gradient(#cfd7c2,#8aa55a)}
.promo .slogan{position:absolute;left:0;width:100%;top:146px;text-align:center;color:#f6c21c;
  font:500 20px "Roboto",sans-serif}
.promo .cta{position:absolute;left:9px;top:176px;width:150px;height:28px;background:var(--orange);
  border-radius:3px;color:var(--white);font-size:12px;display:flex;align-items:center;justify-content:center}
.member-body{height:162px;text-align:center;position:relative}
.avatar{position:absolute;left:46px;top:19px;width:78px;height:78px;border-radius:50%;
  background:linear-gradient(#d9d2c8,#a99a88);border:2px solid #c9c9d6}
.member-body .info{position:absolute;left:0;top:101px;width:100%;font-size:11.5px;line-height:16.5px;color:#333}
.arrow{position:absolute;top:50px}

/* footer */
.footer{left:0;top:950px;width:831px;height:151px;background:var(--footer);text-align:center}
.footer nav{position:absolute;left:0;top:37px;width:100%;font-size:10.5px;color:#eee}
.footer nav a{color:#eee;text-decoration:none;margin:0 3px}
.footer small{position:absolute;left:0;top:63px;width:100%;display:block;text-align:center;font:400 9px "Open Sans",sans-serif;color:#eee}
.footer .icons{position:absolute;top:91px;left:0;width:100%;display:flex;justify-content:center;gap:10px}
.footer .icons span{width:19px;height:19px;background:#eee;border-radius:3px}
</style>
</head>
<body>
<div class="scenery" role="img" aria-label="Illustrated landscape of green hills and trees under a blue sky"></div>

<div class="page">
  <header>
    <div class="abs brand"><span class="brand-mark"></span><span class="brand-name">Kreidetafel.de</span></div>
    <div class="abs tagline">Referate, Hausaufgaben und nette Leute kennen lernen</div>
    <div class="abs phone">
      <svg width="13" height="13" viewBox="0 0 24 24"><path fill="#0d5cb6" d="M6.6 10.8a15 15 0 0 0 6.6 6.6l2.2-2.2c.3-.3.7-.4 1-.2 1.1.4 2.3.6 3.6.6.6 0 1 .4 1 1V20c0 .6-.4 1-1 1A17 17 0 0 1 3 4c0-.6.4-1 1-1h3.5c.6 0 1 .4 1 1 0 1.3.2 2.5.6 3.6.1.3 0 .7-.2 1z"/></svg>
      (907) - 442 - 3150
    </div>
    <div class="abs login">
      <svg width="9" height="10" viewBox="0 0 10 12"><rect x="1" y="5" width="8" height="7" fill="#fff"/><path d="M3 5V3a2 2 0 0 1 4 0" stroke="#fff" stroke-width="1.5" fill="none"/></svg>LOGIN
    </div>
  </header>

  <nav class="abs nav">
    <a>START PAGE</a><a>COMMUNITY</a><a>PRESENTATIONS</a><a>FORUMS</a><a>MEMBERS</a><a style="border-right:0">FLIRT SEARCH</a>
    <div class="social"><span></span><span></span><span></span></div>
    <div class="searchcap">
      <svg style="position:absolute;right:16px;top:11px" width="18" height="18" viewBox="0 0 20 20"><circle cx="8" cy="8" r="6" stroke="#fff" stroke-width="2" fill="none"/><path d="M12.5 12.5l6 6" stroke="#fff" stroke-width="2.4"/></svg>
    </div>
  </nav>

  <section class="box" style="left:13px;top:184px">
    <div class="box-head">COMMUNITY<span class="cap"><svg width="16" height="14"><circle cx="8" cy="4" r="3" fill="#fff"/><rect x="3" y="8" width="10" height="6" rx="2" fill="#fff"/></svg></span></div>
    <ul class="list"><li>Register</li><li>Member Login</li><li>Chat</li><li>Flirtsuche</li><li>Forum</li></ul>
  </section>
  <section class="box" style="left:13px;top:370px">
    <div class="box-head">SCHOOL &amp; UNIVERSITY<span class="cap"><svg width="16" height="14"><path d="M1 5L8 1l7 4z" fill="#fff"/><rect x="2" y="6" width="2" height="6" fill="#fff"/><rect x="7" y="6" width="2" height="6" fill="#fff"/><rect x="12" y="6" width="2" height="6" fill="#fff"/><rect x="1" y="12" width="14" height="2" fill="#fff"/></svg></span></div>
    <ul class="list"><li style="height:40px">Speeches / Housework</li></ul>
  </section>
  <section class="box" style="left:13px;top:454px">
    <div class="box-head">INFORMATION<span class="cap"><svg width="16" height="16"><circle cx="8" cy="8" r="7" fill="#fff"/><rect x="7" y="7" width="2" height="5" fill="#8cc34a"/><circle cx="8" cy="4.5" r="1.2" fill="#8cc34a"/></svg></span></div>
    <ul class="list"><li style="height:41px">FAQs</li></ul>
  </section>
  <section class="box" style="left:13px;top:540px">
    <div class="box-head">STATISTICS<span class="cap"><svg width="16" height="14"><rect x="1" y="13" width="15" height="1" fill="#fff"/><rect x="0" y="1" width="1" height="13" fill="#fff"/><rect x="3" y="7" width="2" height="5" fill="#fff"/><rect x="7" y="3" width="2" height="9" fill="#fff"/><rect x="11" y="5" width="2" height="7" fill="#fff"/></svg></span></div>
    <ul class="list">
      <li>Members<span class="num">401325</span></li>
      <li>Men<span class="num">197695</span></li>
      <li>Women<span class="num">196799</span></li>
      <li>Presentations<span class="num">12458</span></li>
      <li>Posts<span class="num">3080848</span></li>
    </ul>
  </section>

  <div class="abs hero" role="img" aria-label="Photo of a smiling graduate in cap and gown giving a thumbs up">
    <div class="hero-search"><label>KEYWORD:</label><div class="field">Was suchst du? Hier eingeben!</div><div class="btn">SEARCH</div></div>
  </div>
  <div class="abs tree" role="img" aria-label="Illustration of a pencil growing into a tree with colourful school icons"></div>
  <div class="hello">
    <h1>Hello Visitor ,</h1>
    <p>On Kreidetafel.de you will find many papers , specialist work and homework. If you are not able to find a presentation on a topic, you can ask your question in the forum where you are usually helped quickly. <span class="hl">401325 members</span> are already <span class="lk">registered</span> with us!</p>
  </div>

  <section class="abs subjects">
    <div class="box-head">PRESENTATIONS - HOMEWORK - HOMEWORK FOR THE FOLLOWING SUBJECTS:<span class="cap" style="width:52px"><svg width="16" height="16"><circle cx="8" cy="8" r="7" fill="#fff"/><path d="M4 5c2 0 3 2 2 4M10 3c0 3 3 3 3 6" stroke="#8cc34a" stroke-width="1.5" fill="none"/></svg></span></div>
    <div style="position:relative">
      <ul class="col" style="left:10px"><li>English (2937)</li><li>English (1113)</li><li>Latin (275)French (196)</li><li>Italian (32)</li><li>Greek (28)</li><li>Spanish (74)</li><li>Mathematics (99)</li><li>Physics (481)</li><li>Chemistry (450)</li></ul>
      <ul class="col" style="left:161px"><li>Astronomy (82)</li><li>Geography (785)</li><li>History (1870)</li><li>Social Science (555)</li><li>Business (435)</li><li>Right (109)</li><li>Music (448)</li><li>Art (265)</li><li>Religion (521)</li></ul>
      <ul class="col" style="left:299px"><li>Computer science (191)</li><li>Stenography (6)</li><li>Housekeeping (109)</li><li>Sport (136)</li><li>Choir (19)</li><li>Orchestra (5)</li><li>Biology (1237)</li></ul>
    </div>
  </section>

  <section class="box" style="left:650px;top:184px">
    <div class="box-head">LIVE MESSENGER<span class="cap"><svg width="18" height="14"><ellipse cx="7" cy="6" rx="6" ry="4.5" fill="#fff"/><ellipse cx="12" cy="8" rx="5" ry="4" fill="#fff"/></svg></span></div>
    <div class="msg-body">This feature is only available<br>for members.<br><br>Contact Us | <a>Login</a></div>
    <div class="msg-foot">No new message</div>
  </section>

  <section class="abs promo">
    <h3>Dein Kreidetafel.de</h3>
    <div class="photo" role="img" aria-label="Photo of a group of smiling students holding books"></div>
    <div class="slogan">Schon dabei?</div>
    <div class="cta">Kostenlos registrieren</div>
  </section>

  <section class="box" style="left:650px;top:607px">
    <div class="box-head">NEW MEMBER<span class="cap"><svg width="14" height="14"><circle cx="7" cy="4" r="3.5" fill="#fff"/><rect x="1" y="8" width="12" height="6" rx="3" fill="#fff"/></svg></span></div>
    <div class="member-body">
      <svg class="arrow" style="left:22px" width="9" height="14"><path d="M9 0v14L0 7z" fill="#333"/></svg>
      <div class="avatar" role="img" aria-label="Profile photo of the newest member"></div>
      <svg class="arrow" style="right:22px" width="9" height="14"><path d="M0 0v14l9-7z" fill="#333"/></svg>
      <div class="info">Lernfuchs<br>Age: 23 years<br>Profile</div>
    </div>
  </section>

  <footer class="abs footer">
    <nav><a>Home</a>|<a>Department of School - Housework</a>|<a>imprint</a>|<a>data protection</a>|<a>Conditions</a></nav>
    <small>Copyright @ 2017 Kreidetafel.de. All Rights Reserved.</small>
    <div class="icons"><span></span><span></span><span></span><span></span><span></span></div>
  </footer>
</div>
</body>
</html>
```